Out of town New Masters of Accounting

size of ad is 7” x 9.6”
please leave one inch on bottom for footer
We want to attract out of town students to join this master's in accounting program.
You DO NOT  have to use a picture of a person.
But if you do, it should be a  male with a white shirt and should not have long hair.(look like a young executive)
THE TEXT OF THE AD IS IN THE ATTACHMENTS
THE CAP LETTERS ARE THE INSTRUCTIONS

The age we are trying to attract is from 20-30 of ages.
- a clear ad .. the text should not take up the entire ad.. it should not be very crowded -
it should be an attractive ad that people would want to see and stand out
- the text very big and take up the entire ad

```html
<!DOCTYPE html>
<html lang="en">
<head>
<meta charset="utf-8">
<title>Remote Master of Science in Accounting</title>
<link href="https://fonts.googleapis.com/css2?family=Montserrat:wght@400;500;600;700;800;900&display=swap" rel="stylesheet">
<style>
  :root {
    --paper: #f3f3f3;
    --ink: #0a0a0a;
    --white: #ffffff;
    --brand-blue: #208ed9;
    --sky-blue: #36a6f3;
    --accent-blue: #2a8de0;
    --navy: #06345a;
    --star-gold: #ffd500;
    --badge-orange: #f19a1f;
  }
  * { margin: 0; padding: 0; box-sizing: border-box; }
  html, body { width: 846px; height: 1200px; overflow: hidden; background: var(--paper); }
  body { font-family: "Montserrat", sans-serif; color: var(--ink); }
  .ad { position: relative; width: 846px; height: 1200px; background: var(--paper); overflow: hidden; }

  .hero-photo {
    position: absolute; left: 0; top: 0; width: 846px; height: 600px;
    background: linear-gradient(100deg, #efeeec 0%, #ebe9e6 42%, #c9d2dc 62%, #a9bccf 78%, #e6e0d8 100%);
  }
  .ranking-badge {
    position: absolute; left: 705px; top: 44px; width: 82px; height: 82px;
    border-radius: 50%; background: var(--badge-orange);
  }

  .headline { position: absolute; left: 72px; top: 150px; }
  .headline-main { font-size: 61px; font-weight: 900; letter-spacing: -0.5px; line-height: 1; }
  .headline-accent { margin-top: 14px; font-size: 29px; font-weight: 800; color: var(--accent-blue); line-height: 1; }
  .headline-sub { font-size: 28px; font-weight: 800; line-height: 1; margin-top: 2px; }
  .headline-sub span { display: block; margin-bottom: 1px; }

  .offer-panel { position: absolute; left: 48px; top: 457px; width: 374px; height: 608px; background: var(--brand-blue); }
  .start-label { position: absolute; left: 34px; top: 52px; font-size: 15px; font-weight: 500; color: var(--white); }
  .start-date { position: absolute; left: 34px; top: 65px; font-size: 35px; font-weight: 900; line-height: 1.1; letter-spacing: -0.5px; }
  .divider { position: absolute; left: 32px; top: 114px; width: 102px; height: 2px; background: var(--white); }
  .price-note { position: absolute; left: 32px; top: 135px; font-size: 20px; font-weight: 800; color: var(--white); text-decoration: underline; text-underline-offset: 3px; text-decoration-thickness: 1px; }
  .career-title { position: absolute; left: 28px; top: 200px; font-size: 35px; font-weight: 900; line-height: 1.03; letter-spacing: -0.3px; }
  .degree-line { position: absolute; left: 29px; top: 290px; font-size: 27px; font-weight: 500; color: var(--white); line-height: 1.2; }
  .degree-line strong { font-weight: 700; text-decoration: underline; text-underline-offset: 5px; text-decoration-thickness: 1px; }
  .placement-title { position: absolute; left: 29px; top: 398px; font-size: 19px; font-weight: 600; line-height: 1.27; }
  .placement-list { position: absolute; left: 29px; top: 464px; list-style: none; color: var(--white); font-size: 14px; font-weight: 500; }
  .placement-list li { position: relative; padding-left: 17px; margin-bottom: 8px; line-height: 1.2; }
  .placement-list li::before { content: ""; position: absolute; left: 1px; top: 6px; width: 6px; height: 6px; border-radius: 50%; background: var(--white); }

  .rating { position: absolute; left: 467px; top: 648px; width: 330px; }
  .rating-name { font-size: 26px; font-weight: 800; line-height: 1; }
  .rating-stars { margin-top: 7px; color: var(--star-gold); font-size: 22px; letter-spacing: 2px; line-height: 1; }
  .rating-text { margin-top: 9px; font-size: 15.5px; font-weight: 500; line-height: 1.24; }
  .rating-text strong { font-weight: 700; }

  .duration-box { position: absolute; left: 375px; top: 841px; width: 422px; height: 175px; background: var(--sky-blue); }
  .duration-icon { position: absolute; left: 94px; top: 45px; }
  .duration-name { position: absolute; left: 162px; top: 50px; font-size: 24px; font-weight: 900; line-height: 1; }
  .duration-lead { position: absolute; left: 162px; top: 85px; font-size: 15.5px; font-weight: 600; }
  .duration-value { position: absolute; left: 161px; top: 101px; font-size: 27px; font-weight: 900; color: var(--white); }

  .footer-call { position: absolute; left: 47px; top: 1065px; width: 375px; height: 86px; background: var(--navy); }
  .call-label { position: absolute; left: 57px; top: 20px; font-size: 14px; font-weight: 500; color: var(--brand-blue); }
  .call-icon { position: absolute; left: 30px; top: 38px; }
  .call-number { position: absolute; left: 55px; top: 31px; font-size: 32px; font-weight: 500; color: var(--white); letter-spacing: 0.5px; }
  .footer-contact { position: absolute; left: 422px; top: 1065px; width: 375px; height: 86px; background: var(--brand-blue); color: var(--white); font-size: 12px; font-weight: 500; line-height: 1.27; }
  .contact-item { position: absolute; top: 28px; display: flex; gap: 6px; }
  .contact-item svg { flex: none; margin-top: 1px; }
  .contact-address { left: 24px; }
  .contact-web { left: 196px; }
  .contact-web .row { display: flex; gap: 6px; align-items: center; }
</style>
</head>
<body>
<main class="ad">
  <div class="hero-photo" role="img" aria-label="Photo of a young student in glasses and a denim shirt reading an open notebook while holding a pen"></div>
  <div class="ranking-badge" role="img" aria-label="Masters ranking award badge"></div>

  <header class="headline">
    <h1 class="headline-main">ALL NEW!</h1>
    <p class="headline-accent">REMOTE PROGRAM</p>
    <p class="headline-sub"><span>FOR OUT OF TOWN</span><span>STUDENTS</span></p>
  </header>

  <section class="offer-panel">
    <p class="start-label">BEGINNING</p>
    <p class="start-date">AUGUST 17</p>
    <div class="divider"></div>
    <p class="price-note">NEW LOWER PRICES</p>
    <h2 class="career-title">Advance further<br>in your career</h2>
    <p class="degree-line">With a <strong>Masters of</strong><br><strong>Science</strong> in Accounting</p>
    <h3 class="placement-title">Meridian Career Network Job<br>Placement Advantage</h3>
    <ul class="placement-list">
      <li>96% placement rate</li>
      <li>8 placement coordinators</li>
      <li>Decades of relationships with<br>100’s of firm</li>
    </ul>
  </section>

  <section class="rating">
    <h3 class="rating-name">Gradvista</h3>
    <div class="rating-stars" aria-label="Five stars">★★★★★</div>
    <p class="rating-text"><strong>Harwick Dale University (HDU)</strong><br>Master in Accounting Program<br>received the <strong>highest possible<br>star rating.</strong></p>
  </section>

  <section class="duration-box">
    <svg class="duration-icon" width="54" height="54" viewBox="0 0 54 54" fill="none" stroke="#fff" stroke-width="2" stroke-linecap="round" stroke-linejoin="round" aria-hidden="true">
      <path d="M8 40 L36 8 a6 6 0 0 1 10 8 L18 48"/>
      <ellipse cx="12" cy="45" rx="6" ry="4" transform="rotate(-45 12 45)"/>
      <path d="M22 28 l10 9"/>
      <path d="M30 36 c2 4 2 8 4 12"/>
      <path d="M30 36 c4 2 7 3 10 6"/>
    </svg>
    <p class="duration-name">BRIGHTPATH</p>
    <p class="duration-lead">A masters in only</p>
    <p class="duration-value">15 months</p>
  </section>

  <footer>
    <div class="footer-call">
      <p class="call-label">Give us a call</p>
      <svg class="call-icon" width="16" height="24" viewBox="0 0 16 24" fill="none" stroke="#fff" stroke-width="2.4" aria-hidden="true">
        <rect x="2" y="2" width="12" height="20" rx="2"/><line x1="2" y1="17" x2="14" y2="17"/>
      </svg>
      <p class="call-number">900 555 0142</p>
    </div>
    <div class="footer-contact">
      <div class="contact-item contact-address">
        <svg width="10" height="13" viewBox="0 0 10 13" aria-hidden="true"><path d="M5 0a5 5 0 0 1 5 5c0 3.5-5 8-5 8S0 8.5 0 5a5 5 0 0 1 5-5z" fill="#fff"/><circle cx="5" cy="5" r="1.8" fill="#208ed9"/></svg>
        <p>48 Harlow Av.<br>Fenmore, FL 200410</p>
      </div>
      <div class="contact-item contact-web">
        <div>
          <div class="row"><svg width="12" height="12" viewBox="0 0 12 12" fill="none" stroke="#fff" stroke-width="1.4" aria-hidden="true"><circle cx="6" cy="6" r="2.2"/><path d="M8.2 4v2.8c0 1.6 2.8 1.6 2.8-.8A5 5 0 1 0 8 10.6"/></svg><span>support@example.com</span></div>
          <div class="row"><svg width="12" height="12" viewBox="0 0 12 12" fill="none" stroke="#fff" stroke-width="1.2" aria-hidden="true"><circle cx="6" cy="6" r="5"/><path d="M1 6h10M6 1c-2.5 3-2.5 7 0 10M6 1c2.5 3 2.5 7 0 10"/></svg><span>www.example.com</span></div>
        </div>
      </div>
    </div>
  </footer>
</main>
</body>
</html>
```